Verdant Loop Advisors, LLC

I am looking for a simple, clear layout with my logo prominent and embossed, on the best quality card stock available. I would like the business name and phone number included on the card as well......I dont want my name anywhere on the card and I would like my logo embossed on the card......something simple with a white back......open to designs as long as they go along with recycling symbols and green type stuff.....The address, website, cell number, fax number, and email are listed below

5374 Tillbury Fenwood Road
Fenwick Glen, MD 20999

c. 240.555.0143 f. 240.555.0187
e. sales@verdantloopadvisors.example
w. www.verdantloopadvisors.example

Industry/Entity Type

Recycling

```html
<!DOCTYPE html>
<html lang="en">
<head>
<meta charset="utf-8">
<title>Verdant Loop Advisors, LLC — Business Card</title>
<link rel="stylesheet" href="https://fonts.googleapis.com/css2?family=Montserrat:wght@300;400;700&display=swap">
<style>
  :root {
    --backdrop: #e6e7e9;
    --card: #f7f7f8;
    --brand-green: #1f5e2a;
    --ink: #2a2620;
    --soft-green: #4f7d55;
    --shadow: rgba(0, 0, 0, 0.12);
  }
  * { box-sizing: border-box; margin: 0; padding: 0; }
  html, body {
    width: 1200px; height: 720px; overflow: hidden;
    background: var(--backdrop);
    font-family: "Montserrat", sans-serif;
  }
  .canvas {
    position: relative; width: 1200px; height: 720px;
    display: flex; align-items: center; justify-content: center; gap: 50px;
  }
  .card {
    position: relative; width: 540px; height: 309px;
    background: var(--card);
    box-shadow: 0 10px 28px var(--shadow);
  }
  /* brand block: plain square above the name set as text */
  .brand {
    display: flex; flex-direction: column; align-items: center; gap: 14px;
    text-align: center;
  }
  .brand-mark {
    width: 96px; height: 96px; background: var(--brand-green); flex: none;
  }
  .brand-name {
    font-weight: 700; color: var(--ink);
    text-transform: uppercase; letter-spacing: 0.04em; line-height: 1.2;
  }
  /* front */
  .card-front .brand {
    position: absolute; left: 20px; top: 70px; width: 200px;
  }
  .card-front .brand-name { font-size: 14px; }
  .divider {
    position: absolute; left: 238px; top: 44px; width: 3px; height: 221px;
    background: var(--brand-green);
  }
  .contact {
    position: absolute; left: 266px; top: 64px; width: 260px;
  }
  .address {
    font-weight: 700; font-size: 11.5px; color: var(--brand-green);
    text-transform: uppercase; line-height: 1.75; letter-spacing: 0.01em;
  }
  .details { margin-top: 24px; list-style: none; }
  .details li {
    display: flex; font-size: 10px; line-height: 2.05;
    text-transform: uppercase; font-weight: 300; color: var(--soft-green);
    white-space: nowrap;
  }
  .details .label {
    width: 22px; font-weight: 700; color: var(--ink);
  }
  /* back */
  .card-back { display: flex; align-items: center; justify-content: center; }
  .card-back .brand-mark { width: 130px; height: 130px; }
  .card-back .brand-name { font-size: 20px; }
</style>
</head>
<body>
<main class="canvas">
  <section class="card card-front" aria-label="Business card front">
    <div class="brand">
      <span class="brand-mark" aria-hidden="true"></span>
      <span class="brand-name">Verdant Loop<br>Advisors, LLC</span>
    </div>
    <div class="divider" aria-hidden="true"></div>
    <div class="contact">
      <p class="address">5374 Tillbury Fenwood Road<br>Fenwick Glen, MD 20999</p>
      <ul class="details">
        <li><span class="label">C:</span>240.555.0143</li>
        <li><span class="label">F:</span>240.555.0187</li>
        <li><span class="label">E:</span>sales@verdantloopadvisors.example</li>
        <li><span class="label">W:</span>www.verdantloopadvisors.example</li>
      </ul>
    </div>
  </section>
  <section class="card card-back" aria-label="Business card back">
    <div class="brand">
      <span class="brand-mark" aria-hidden="true"></span>
      <span class="brand-name">Verdant Loop<br>Advisors, LLC</span>
    </div>
  </section>
</main>
</body>
</html>
```